Webpage - LORAVENNE.COM (Webpage)

Design webpage for LoraVenne.com (already own the domain).
At a minimum the webpage should include links and information about:
1. BRAND - https://kelpmoonliving.example/
2. SONGS – link to artist and all released songs (3 currently available under Lora Venne on Tunewell and other platforms). Ability to add songs as they are released.
3. PODCAST - Links to existing (2) and upcoming podcasts "Days Run Crooked" (currently available on Tunewell, Reelcast and other platforms). Ability to add links to future podcasts.
https://video.example/watch?v=Qb3TzLw8Rk0
4. VOICE COACH - Information about voice coaching/lessons by Lora Venne as well as how to contact regarding the lessons. Ability to add testimonials. Add "click here" link for requesting more information regarding voice lessons, with fields like name, email, cell phone and best method, time to contact that user can fill to request info
5. SOCIAL MEDIA -Links to Lora Venne's Glimmerly, Neighborly, Loopster, Reelcast Channel (not yet created), etc.
6. BAND - Link to access information about band “Lora Venne and HOLLXWPINE
https://social.example/hollxwpineband/?next=%2Fgrutelmosa%2Ffeed%2F&locale=en_US%2Cen_US. Add "click here" link for requesting more information regarding voice lessons, with fields like name, email, cell phone and best method, time to contact that user can fill to request info
7. VIDEOS – links to music and promotional videos from solo artist and band. All will eventually be compiled on Reelcast channel.
Pictures are included for reference and use but not necessarily asking that they all be on the website. Designer can use discretion from uploaded files or request more if desired.

Coding

Number of Pages Required

1 page

Requirements
Must have
• Original artist song plays when opening page. Preferably Turn Tide Turn Home or PBR.
Nice to have
• Rotating songs play when clicking any link

```html
<!DOCTYPE html>
<html lang="en">
<head>
<meta charset="utf-8">
<title>Lora Venne</title>
<link href="https://fonts.googleapis.com/css2?family=Poppins:wght@400;500;600&family=Yellowtail&display=swap" rel="stylesheet">
<style>
:root{
  --bg:#1e1d1f;
  --bg-deep:#18171a;
  --footer:#232124;
  --card:#2a282b;
  --row:#2b292c;
  --gold:#c99a2e;
  --gold-soft:#d9ab3a;
  --white:#ffffff;
  --text:#c4c2c6;
  --muted:#9c999f;
  --green:#3fbf5f;
  --red:#e0282e;
}
*{margin:0;padding:0;box-sizing:border-box}
html,body{width:1200px;height:4263px;overflow:hidden;background:var(--bg)}
body{font-family:'Poppins',sans-serif;color:var(--text)}
.page{position:relative;width:1200px;height:4263px;overflow:hidden;
  background:
   radial-gradient(ellipse 520px 380px at 900px 1500px,rgba(90,40,90,.35),transparent 70%),
   radial-gradient(ellipse 600px 300px at 300px 1650px,rgba(70,30,70,.25),transparent 70%),
   var(--bg)}
.abs{position:absolute}
.script{font-family:'Yellowtail',cursive;font-weight:400;color:var(--white);line-height:1}
.script em{font-style:normal;color:var(--gold)}
a{color:inherit;text-decoration:none}

/* header */
.site-header{left:0;top:0;width:1200px;height:101px;background:var(--bg-deep)}
.brand{left:116px;top:28px;font-size:36px;font-weight:600;color:var(--white);letter-spacing:.5px}
.util{top:38px;display:flex;align-items:center;gap:12px;font-size:14px;font-weight:500;color:var(--white)}
.util .dot{width:26px;height:26px;border-radius:50%;background:#2f2d31;display:flex;align-items:center;justify-content:center}
.main-nav{left:0;top:101px;width:1200px;height:41px;background:var(--gold)}
.main-nav a{position:absolute;top:13px;font-size:12px;font-weight:500;color:#1c1b1d}
.main-nav a.active{text-decoration:underline}

/* hero */
.hero{left:0;top:142px;width:1200px;height:469px;background:linear-gradient(90deg,#3a3a3c 0%,#5c5c5e 45%,#8d8d8f 100%)}
.hero-photo{left:520px;top:142px;width:680px;height:469px;background:radial-gradient(ellipse at 60% 55%,#a8a8aa,#6a6a6c 60%,#4e4e50)}
.hero-shade{left:0;top:142px;width:760px;height:469px;background:linear-gradient(90deg,rgba(40,40,42,.95),rgba(40,40,42,.6) 70%,transparent)}
.hero-title{left:112px;top:212px;font-size:58px;line-height:75px}
.hero-copy{left:111px;top:372px;width:400px;font-size:14px;line-height:33px;color:var(--white)}
.btn-outline{display:inline-flex;align-items:center;justify-content:center;border:1.5px solid var(--white);color:var(--white);font-size:14px;font-weight:500}
.btn-gold{display:inline-flex;align-items:center;justify-content:center;border:1.5px solid var(--gold);color:var(--gold);font-size:14px;font-weight:500}

.section-title{left:0;width:1200px;text-align:center;font-size:46px}

/* songs */
.song{left:111px;width:978px;height:52px;background:var(--row);font-size:13px;font-weight:500;color:var(--white)}
.song span{position:absolute;top:17px}
.song .name{left:30px;color:var(--gold)}
.song .sep{left:490px}
.song .play{left:819px;top:15px;width:78px;height:22px;border:1px solid var(--gold);color:var(--gold);font-size:9px;display:flex;align-items:center;justify-content:center}
.song .chip{left:921px;top:15px;width:22px;height:22px;border-radius:50%;background:var(--green)}
.song.current{background:var(--gold);color:#1c1b1d}
.song.current .name{color:#1c1b1d}
.song.current .play{border-color:#1c1b1d;color:#1c1b1d}
.song.current .chip{background:#1c1b1d}

/* podcast */
.sub-title{font-size:40px}
.photo{border-radius:4px}
.ep-label{font-size:15px;font-weight:500;color:var(--white)}
.ep-title{font-size:18px;line-height:32px;color:var(--gold);width:240px}
.ep-body{font-size:13.5px;line-height:33px;color:var(--white);width:250px}
.ep-play{display:flex;align-items:center;gap:16px;font-size:14px;font-weight:500;color:var(--gold)}
.badge{width:26px;height:26px;border-radius:50%;border:3px solid var(--white)}

/* body text */
.copy{font-size:14px;line-height:37px;color:var(--text)}

/* testimonials */
.t-card{top:2423px;width:316px;height:405px;background:var(--card)}
.t-card .shot{position:absolute;left:13px;top:13px;width:290px;height:189px}
.t-card .avatar{position:absolute;left:35px;top:168px;width:72px;height:72px;border-radius:50%;background:#5a6a80;border:3px solid var(--card)}
.t-card p{position:absolute;left:35px;top:260px;width:250px;font-size:13.5px;line-height:33px;color:var(--text)}
.t-card .who{position:absolute;left:35px;top:366px;font-size:17px;font-weight:500;color:var(--gold)}
.t-card .stars{position:absolute;right:25px;top:367px;font-size:14px;color:var(--white);letter-spacing:2px}
.round{width:28px;height:28px;border-radius:50%;display:flex;align-items:center;justify-content:center}

/* footer */
.site-footer{left:0;top:3990px;width:1200px;height:273px;background:var(--footer)}
.f-head{font-size:20px;font-weight:500;color:var(--gold)}
.f-link{font-size:14px;color:var(--white)}
</style>
</head>
<body>
<div class="page">

  <header class="abs site-header">
    <a class="abs brand" href="#">Lora Venne</a>
    <a class="abs util" style="left:840px" href="#"><span class="dot"><svg width="12" height="12" viewBox="0 0 12 12" fill="none" stroke="#fff" stroke-width="1.2"><circle cx="6" cy="4" r="2.3"/><path d="M1.8 11c.5-2.4 2.2-3.6 4.2-3.6s3.7 1.2 4.2 3.6"/></svg></span>LOGIN</a>
    <a class="abs util" style="left:980px" href="#"><span class="dot"><svg width="12" height="12" viewBox="0 0 12 12" fill="none" stroke="#fff" stroke-width="1.3"><circle cx="5" cy="5" r="3.3"/><path d="M7.5 7.5l3 3"/></svg></span>SEARCH</a>
  </header>

  <nav class="abs main-nav">
    <a class="active" style="left:176px" href="#">HOME</a>
    <a style="left:272px" href="#">ABOUT</a>
    <a style="left:374px" href="#">MUSIC</a>
    <a style="left:471px" href="#">PODCAST</a>
    <a style="left:592px" href="#">VOICE COACHING</a>
    <a style="left:760px" href="#">BAND</a>
    <a style="left:855px" href="#">VIDEOS</a>
    <a style="left:959px" href="#">CONTACT</a>
  </nav>

  <section>
    <div class="abs hero"></div>
    <div class="abs hero-photo" role="img" aria-label="Black and white photo of the band posing with instruments"></div>
    <div class="abs hero-shade"></div>
    <h1 class="abs script hero-title">The Sound <em>The Voice</em><br>The Journey</h1>
    <p class="abs hero-copy">Lorem ipsum dolor sit amet, consectetur adipiscing elit, sed do eiusmod tempor incididunt ut labore et dolore magna aliqua.</p>
    <a class="abs btn-outline" style="left:111px;top:500px;width:132px;height:40px" href="#">LISTEN NOW</a>
  </section>

  <section>
    <h2 class="abs script section-title" style="top:682px">Stay Tuned <em>For</em> More Music</h2>
    <div class="abs song" style="top:773px"><span class="name">SONG TITLE 1</span><span style="left:215px">RELEASE DATE: DECEMBER 1, 2024</span><span style="left:521px">LOREM IPSUM DOLOR SIT AMET</span><a class="abs play" href="#">PLAY NOW</a><span class="chip" role="img" aria-label="Tunewell"></span></div>
    <div class="abs song current" style="top:841px"><span class="name">SONG TITLE 2</span><span style="left:215px">RELEASE DATE: DECEMBER 8, 2024</span><span class="sep">|</span><span style="left:526px">LOREM IPSUM DOLOR SIT AMET</span><a class="abs play" href="#">PLAY NOW</a><span class="chip" role="img" aria-label="Tunewell"></span></div>
    <div class="abs song" style="top:910px"><span class="name">SONG TITLE 3</span><span style="left:215px">RELEASE DATE: DECEMBER 6, 2024</span><span class="sep">|</span><span style="left:526px">LOREM IPSUM DOLOR SIT AMET</span><a class="abs play" href="#">PLAY NOW</a><span class="chip" role="img" aria-label="Tunewell"></span></div>
  </section>

  <section>
    <h2 class="abs script sub-title" style="left:112px;top:1040px">Our <em>Podcast</em></h2>
    <h2 class="abs script sub-title" style="left:659px;top:1040px">Upcoming <em>Podcasts</em></h2>
    <h3 class="abs script sub-title" style="left:659px;top:1112px"><em>Days Run Crooked</em></h3>

    <div class="abs photo" style="left:112px;top:1132px;width:197px;height:237px;background:linear-gradient(135deg,#5b4a3a,#3a4a5c 60%,#2c2a2e)" role="img" aria-label="Photo of the band on a couch with instruments"></div>
    <span class="abs badge" style="left:267px;top:1143px;background:var(--green)"></span>
    <span class="abs badge" style="left:267px;top:1183px;background:var(--red)"></span>
    <div class="abs ep-label" style="left:346px;top:1128px">EPISODE 1</div>
    <div class="abs ep-title" style="left:344px;top:1157px">LOREM IPSUM DOLOR SIT AMET, CONSECTETUR</div>
    <p class="abs ep-body" style="left:344px;top:1224px">Lorem ipsum dolor sit amet, consectetur adipiscing elit, sed do eiusmod tempor incididunt ut</p>
    <a class="abs ep-play" style="left:344px;top:1342px" href="#"><svg width="28" height="28" viewBox="0 0 28 28"><circle cx="14" cy="14" r="14" fill="#c99a2e"/><path d="M11 9l8 5-8 5z" fill="#1e1d1f"/></svg>PLAY EPISODE</a>

    <div class="abs photo" style="left:112px;top:1413px;width:197px;height:237px;background:linear-gradient(160deg,#4a4446,#2a2729 70%)" role="img" aria-label="Photo of the singer performing with a microphone"></div>
    <span class="abs badge" style="left:267px;top:1424px;background:var(--green)"></span>
    <span class="abs badge" style="left:267px;top:1464px;background:var(--red)"></span>
    <div class="abs ep-label" style="left:346px;top:1409px">EPISODE 2</div>
    <div class="abs ep-title" style="left:344px;top:1438px">LOREM IPSUM DOLOR SIT AMET, CONSECTETUR</div>
    <p class="abs ep-body" style="left:344px;top:1505px">Lorem ipsum dolor sit amet, consectetur adipiscing elit, sed do eiusmod tempor incididunt ut</p>
    <a class="abs ep-play" style="left:344px;top:1623px" href="#"><svg width="28" height="28" viewBox="0 0 28 28"><circle cx="14" cy="14" r="14" fill="#c99a2e"/><path d="M11 9l8 5-8 5z" fill="#1e1d1f"/></svg>PLAY EPISODE</a>

    <div class="abs" style="left:659px;top:1193px;width:430px;height:247px;background:linear-gradient(90deg,#7a2a22,#5a3626 50%,#3a2a40)" role="img" aria-label="Podcast episode one video thumbnail with two hosts at microphones"></div>
    <a class="abs btn-gold" style="left:736px;top:1476px;width:275px;height:38px;font-size:14px" href="#">SUBSCRIBE FOR NEW EPISODES</a>
    <span class="abs badge" style="left:835px;top:1551px;width:28px;height:28px;background:var(--green)"></span>
    <span class="abs badge" style="left:886px;top:1551px;width:28px;height:28px;background:var(--red)"></span>
  </section>

  <section>
    <h2 class="abs script section-title" style="top:1722px">Voice <em>Coaching</em></h2>
    <div class="abs" style="left:126px;top:1834px;width:442px;height:418px;border-right:2px solid var(--gold);border-bottom:2px solid var(--gold)"></div>
    <div class="abs" style="left:111px;top:1820px;width:445px;height:421px;background:linear-gradient(135deg,#3c3a2e,#2a3028 50%,#4a4640)" role="img" aria-label="Band members in white outfits posing with instruments among plants"></div>
    <div class="abs copy" style="left:622px;top:1809px;width:470px">
      <p>Lorem ipsum dolor sit amet, consectetur adipiscing elit, sed do eiusmod tempor incididunt ut labore et dolore magna aliqua. Ut enim ad minim veniam, quis nostrud exercitation ullamco laboris nisi ut aliquip ex ea commodo consequat. Duis aute irure dolor in reprehenderit in voluptate velit esse cillum dolore eu fugiat nulla pariatur. Excepteur sint occaecat cupidatat non proident, sunt in culpa qui officia deserunt mollit anim id est laborum.</p>
      <p style="margin-top:8px">Lorem ipsum dolor sit amet, consectetur adipiscing elit, sed do eiusmod tempor incididunt ut labore et dolore magna aliqua.</p>
    </div>
    <a class="abs btn-gold" style="left:622px;top:2208px;width:262px;height:40px" href="#">START YOUR VOICE JOURNEY</a>
  </section>

  <section>
    <h2 class="abs script sub-title" style="left:112px;top:2328px">Our <em>Testimonials</em></h2>
    <a class="abs round" style="left:1008px;top:2338px;background:var(--white)" href="#"><svg width="10" height="12" viewBox="0 0 10 12"><path d="M7 1L2 6l5 5" fill="none" stroke="#1e1d1f" stroke-width="2.2"/></svg></a>
    <a class="abs round" style="left:1060px;top:2338px;background:var(--gold)" href="#"><svg width="10" height="12" viewBox="0 0 10 12"><path d="M3 1l5 5-5 5" fill="none" stroke="#1e1d1f" stroke-width="2.2"/></svg></a>

    <article class="abs t-card" style="left:111px">
      <div class="shot" style="background:linear-gradient(180deg,#3a6a78,#2a3a30 60%,#5a3a30)" role="img" aria-label="Band performing on a festive stage"></div>
      <div class="avatar" role="img" aria-label="Reviewer portrait"></div>
      <p>“Lorem ipsum dolor sit amet, consectetur adipiscing elit, sed do eiusmod tempor ”</p>
      <span class="who">JOHN DOE</span><span class="stars">★★★★★</span>
    </article>
    <article class="abs t-card" style="left:442px">
      <div class="shot" style="background:linear-gradient(135deg,#3a1c22,#7a2a36 50%,#2a1a20)" role="img" aria-label="Singer on stage under red lights"></div>
      <div class="avatar" role="img" aria-label="Reviewer portrait"></div>
      <p>“Lorem ipsum dolor sit amet, consectetur adipiscing elit, sed do eiusmod tempor ”</p>
      <span class="who">JOHN DOE</span><span class="stars">★★★★★</span>
    </article>
    <article class="abs t-card" style="left:773px">
      <div class="shot" style="background:linear-gradient(135deg,#c83a1a,#8a1a10 60%,#3a1010)" role="img" aria-label="Singer performing in front of a red event poster"></div>
      <div class="avatar" role="img" aria-label="Reviewer portrait"></div>
      <p>“Lorem ipsum dolor sit amet, consectetur adipiscing elit, sed do eiusmod tempor ”</p>
      <span class="who">JOHN DOE</span><span class="stars">★★★★★</span>
    </article>
  </section>

  <section>
    <h2 class="abs script section-title" style="top:2900px">Our <em>Videos</em></h2>
    <div class="abs" style="left:179px;top:2994px;width:842px;height:323px;border-radius:8px;background:linear-gradient(90deg,#2e2a24,#4a5a6a 35%,#3a3028 65%,#4a4a52)" role="img" aria-label="Music video still of the band with instruments"></div>
    <svg class="abs" style="left:570px;top:3125px" width="60" height="60" viewBox="0 0 60 60"><circle cx="30" cy="30" r="30" fill="#fff"/><path d="M24 19l17 11-17 11z" fill="#c99a2e"/></svg>
    <svg class="abs" style="left:106px;top:3143px" width="16" height="24" viewBox="0 0 16 24"><path d="M12 2L3 12l9 10" fill="none" stroke="#fff" stroke-width="2.5"/></svg>
    <svg class="abs" style="left:1066px;top:3143px" width="16" height="24" viewBox="0 0 16 24"><path d="M4 2l9 10-9 10" fill="none" stroke="#fff" stroke-width="2.5"/></svg>
  </section>

  <section>
    <h2 class="abs script section-title" style="top:3388px">The Band Lora Venne <em>and Hollxwpine</em></h2>
    <div class="abs copy" style="left:112px;top:3474px;width:470px">
      <p>Lorem ipsum dolor sit amet, consectetur adipiscing elit, sed do eiusmod tempor incididunt ut labore et dolore magna aliqua. Ut enim ad minim veniam, quis nostrud exercitation ullamco laboris nisi ut aliquip ex ea commodo consequat. Duis aute irure dolor in reprehenderit in voluptate velit esse cillum dolore eu fugiat nulla pariatur. Excepteur sint occaecat cupidatat non proident, sunt in culpa qui officia deserunt mollit anim id est laborum.</p>
      <p style="margin-top:8px">Lorem ipsum dolor sit amet, consectetur adipiscing elit, sed do eiusmod tempor incididunt ut labore et dolore magna aliqua.</p>
    </div>
    <a class="abs btn-gold" style="left:112px;top:3874px;width:274px;height:40px" href="#">LEARN MORE ABOUT THE BAND</a>
    <div class="abs" style="left:645px;top:3500px;width:444px;height:419px;border-right:2px solid var(--gold);border-bottom:2px solid var(--gold)"></div>
    <div class="abs" style="left:632px;top:3487px;width:444px;height:419px;background:linear-gradient(90deg,#2a2e36,#5a6270 50%,#2a2e36)" role="img" aria-label="Singer posing in a lit tunnel entrance"></div>
  </section>

  <footer class="abs site-footer">
    <a class="abs brand" style="left:149px;top:58px" href="#">Lora Venne</a>
    <p class="abs" style="left:153px;top:160px;font-size:12px;font-weight:500;color:var(--white)">©2024 COPYRIGHTS.ALL RIGHTS RESERVED</p>
    <h4 class="abs f-head" style="left:571px;top:49px">QUICK LINKS</h4>
    <a class="abs f-link" style="left:571px;top:108px" href="#">Home</a>
    <a class="abs f-link" style="left:571px;top:143px" href="#">About</a>
    <a class="abs f-link" style="left:571px;top:178px" href="#">Music</a>
    <a class="abs f-link" style="left:571px;top:214px" href="#">Podcast</a>
    <a class="abs f-link" style="left:693px;top:108px" href="#">Voice Coaching</a>
    <a class="abs f-link" style="left:693px;top:143px" href="#">Band</a>
    <a class="abs f-link" style="left:693px;top:178px" href="#">Videos</a>
    <a class="abs f-link" style="left:693px;top:214px" href="#">Contact</a>
    <h4 class="abs f-head" style="left:928px;top:49px">FOLLOW US</h4>
    <a class="abs f-link" style="left:928px;top:108px" href="#">Glimmerly</a>
    <a class="abs f-link" style="left:928px;top:143px" href="#">Neighborly</a>
    <a class="abs f-link" style="left:928px;top:178px" href="#">Loopster</a>
    <a class="abs f-link" style="left:928px;top:214px" href="#">Reelcast</a>
  </footer>

</div>
</body>
</html>
```